Business Cards for Corvantis LLC

We need business cards for a new company called “Corvantis LLC”. This is a technology process improvement company providing a comprehensive assessment of the technology used to run their business. The documentation and review process delivers the visibility and reassurance they need to protect their business and plan for the future. The product is called “Halvorne Ledgerwork”. Our primary target is small-medium size businesses, with the deliverables going to the decision maker. We would like to see the designs use the color blue. Our tag line is PROTECT YOUR BUSINESS · TAKE CONTROL OF IT.

Industry/Entity Type

Business

Contact Information for Business Card

Tag line should be on back of card - it does not have to be upper case.

Requirements
Must have
• Please use information when laying out card:
• Name: Darnell Pruitt
• Title: Partner
• Phone Number: (877)555-0143
• Email: dell@corvantisllc.com
• Website: http://corvantisllc.com

```html
<!DOCTYPE html>
<html lang="en">
<head>
<meta charset="utf-8">
<title>Corvantis LLC — Business Cards</title>
<link rel="stylesheet" href="https://fonts.googleapis.com/css2?family=Lato:wght@400;700;900&display=swap">
<style>
  :root {
    --page-bg: #ececec;
    --brand-blue: #1172b8;
    --deep-blue: #0757a5;
    --name-blue: #0b5aa6;
    --accent-yellow: #fdb94a;
    --card-white: #fafafa;
    --ink: #1d1d1d;
    --logo-grey: #7a7a7a;
    --white: #ffffff;
  }
  * { margin: 0; padding: 0; box-sizing: border-box; }
  html, body {
    width: 1200px;
    height: 586px;
    overflow: hidden;
    background: var(--page-bg);
    font-family: "Lato", Arial, sans-serif;
  }
  .canvas {
    position: relative;
    width: 1200px;
    height: 586px;
  }
  .card {
    position: absolute;
    top: 129px;
    width: 501px;
    height: 300px;
    overflow: hidden;
  }
  .card--back {
    left: 61px;
    background: var(--brand-blue);
    color: var(--white);
  }
  .card--front {
    left: 619px;
    background: var(--card-white);
  }

  /* Wordmark: name in one colour and weight */
  .wordmark {
    position: absolute;
    display: flex;
    align-items: center;
    gap: 12px;
    font-weight: 900;
    letter-spacing: 2px;
    text-transform: uppercase;
    white-space: nowrap;
  }
  .wordmark__square {
    width: 30px;
    height: 30px;
    background: currentColor;
  }
  .card--back .wordmark {
    left: 50%;
    top: 132px;
    transform: translateX(-50%);
    font-size: 34px;
    color: var(--white);
  }
  .card--front .wordmark {
    right: 40px;
    top: 100px;
    font-size: 28px;
    color: var(--brand-blue);
  }
  .card--front .wordmark__square { width: 24px; height: 24px; }

  .tagline {
    position: absolute;
    left: 0;
    right: 0;
    top: 254px;
    text-align: center;
    font-size: 12px;
    letter-spacing: 2px;
  }

  .contact-name {
    position: absolute;
    left: 28px;
    top: 167px;
    font-size: 17px;
    font-weight: 700;
    color: var(--name-blue);
  }
  .contact-title {
    position: absolute;
    left: 28px;
    top: 190px;
    font-size: 11px;
    color: var(--ink);
  }
  .contact-list {
    position: absolute;
    left: 28px;
    top: 214px;
    list-style: none;
  }
  .contact-item {
    display: flex;
    align-items: center;
    gap: 8px;
    height: 24px;
    font-size: 12px;
    color: var(--ink);
  }
  .contact-icon { width: 18px; height: 18px; }

  .swoosh {
    position: absolute;
    left: 0;
    top: 0;
    width: 501px;
    height: 300px;
  }
  .website {
    position: absolute;
    right: 17px;
    bottom: 11px;
    font-size: 11.5px;
    font-weight: 700;
    letter-spacing: 1.2px;
    color: var(--white);
  }
</style>
</head>
<body>
<main class="canvas">

  <section class="card card--back" aria-label="Card back">
    <div class="wordmark"><span class="wordmark__square"></span>Corvantis LLC</div>
    <p class="tagline">Protect your Business · Take Control of it.</p>
  </section>

  <section class="card card--front" aria-label="Card front">
    <svg class="swoosh" viewBox="0 0 501 300" aria-hidden="true">
      <path d="M109,274 Q330,264 501,222 L501,238 Q330,270 109,275 Z" fill="var(--accent-yellow)"/>
      <path d="M0,279 Q270,276 501,248 L501,300 L0,300 Z" fill="var(--deep-blue)"/>
    </svg>

    <div class="wordmark"><span class="wordmark__square"></span>Corvantis LLC</div>

    <h1 class="contact-name">Darnell Pruitt</h1>
    <p class="contact-title">Partner</p>

    <ul class="contact-list">
      <li class="contact-item">
        <svg class="contact-icon" viewBox="0 0 18 18" aria-hidden="true">
          <circle cx="9" cy="9" r="9" fill="var(--deep-blue)"/>
          <path d="M4.5,7.5 Q9,4 13.5,7.5 L12.5,9 L11,8.2 L11,7.4 Q9,6.6 7,7.4 L7,8.2 L5.5,9 Z" fill="var(--white)"/>
          <rect x="6" y="9.2" width="6" height="3.8" rx="0.6" fill="var(--white)"/>
        </svg>
        <span>(877)555-0143</span>
      </li>
      <li class="contact-item">
        <svg class="contact-icon" viewBox="0 0 18 18" aria-hidden="true">
          <circle cx="9" cy="9" r="9" fill="var(--deep-blue)"/>
          <rect x="4.5" y="5.8" width="9" height="6.4" fill="var(--white)"/>
          <path d="M4.5,5.8 L9,9.6 L13.5,5.8" fill="none" stroke="var(--deep-blue)" stroke-width="0.9"/>
        </svg>
        <span>dell@corvantisllc.com</span>
      </li>
    </ul>

    <p class="website">www.corvantisllc.com</p>
  </section>

</main>
</body>
</html>
```